PPT template for BLQ. Whiskey, wine, food, drink and music. Moments in time

Lantern Oak and Barrels. Liquor, food, music. Need slides for BLQ, Liquor, food and music.

Think whiskey distillery meets music studio.

Its about moments in time with the people we love. Music, food and drink all play apart in the times we remember.

Target Market(s)

Investors

Industry/Entity Type

Entertainment

Colors

Designer to choose colors to be used in the design.

Requirements
Must have
• Utilize the logo or image without text in all slides.
Nice to have
• blank template pages with logo or just image. multiple versions I can utilize. Logo and image as backgrounds, logo in corner and so on. Logo in many colors, rainbow, nautilus shell. Golden ratio....
Should not have
• Do not need close ups of food. its about people and experiences and food is part of this. Think tables, parties, events, chocolate fountains, and so on

```html
<!DOCTYPE html>
<html lang="en">
<head>
<meta charset="utf-8">
<title>BLQ — Lantern Oak and Barrels slide templates</title>
<link href="https://fonts.googleapis.com/css2?family=Prata&family=Archivo+Black&family=Montserrat:wght@400;600&family=Open+Sans:wght@400&display=swap" rel="stylesheet">
<style>
  :root {
    --board: #e8e8e8;
    --navy: #2b2a8a;
    --royal: #1550b5;
    --white: #ffffff;
    --lavender: #e7e7f3;
    --gold: #c9a968;
    --ink: #111122;
    --photo-dark: #4a4438;
    --photo-light: #e9e6e2;
    --serif: 'Prata', Georgia, serif;
    --display: 'Archivo Black', 'Arial Black', sans-serif;
    --label: 'Montserrat', Arial, sans-serif;
    --body: 'Open Sans', Arial, sans-serif;
  }
  * { margin: 0; padding: 0; box-sizing: border-box; }
  html, body { width: 1200px; height: 675px; overflow: hidden; background: var(--board); }
  .board {
    position: absolute; left: 110px; top: 112px;
    display: grid; grid-template-columns: repeat(4, 241px); grid-template-rows: repeat(3, 136px);
    column-gap: 9px; row-gap: 8px;
  }
  .slide {
    position: relative; width: 241px; height: 136px; overflow: hidden;
    box-shadow: 0 3px 6px rgba(0,0,0,.22);
  }
  .slide > * { position: absolute; }
  .blue-bg { background: linear-gradient(180deg, var(--navy) 0%, var(--royal) 100%); }
  .white-bg { background: var(--white); }
  .page-no { right: 19px; bottom: 6px; font: 400 2.5px var(--label); color: #999; }
  .page-no.light { color: rgba(255,255,255,.5); }

  /* brand name lockup */
  .brand { display: flex; align-items: center; gap: 3px; font-family: var(--serif); }
  .brand .dot { width: 9px; height: 9px; border-radius: 50%; background: currentColor; display: block; }
  .brand .name { letter-spacing: 1px; }

  .deco-circle { border-radius: 50%; }
  .photo { background-size: cover; }

  .deck-title { font-family: var(--serif); letter-spacing: 1.2px; text-transform: uppercase; line-height: 1.05; }
  .deck-sub { font: 600 2.6px var(--label); letter-spacing: 1.2px; text-transform: uppercase; }

  .card-title { font: 400 8px var(--display); letter-spacing: .2px; }
  .card-sub { font: 600 3px var(--label); letter-spacing: 1px; text-transform: uppercase; margin-top: 1px; }
  .card-body { font: 400 2.8px/1.45 var(--body); margin-top: 4px; width: 64px; text-align: justify; }
</style>
</head>
<body>
<main class="board">

  <!-- 1 -->
  <section class="slide white-bg">
    <div class="deco-circle" style="left:43px;top:0;width:160px;height:136px;border:20px solid var(--lavender);border-radius:50%"></div>
    <div style="left:0;right:0;top:48px;text-align:center;color:var(--navy)">
      <div class="brand" style="justify-content:center;font-size:16px"><span class="dot"></span><span class="name">BLQ</span></div>
      <div class="deck-sub" style="margin-top:3px;font-size:3px">Lantern Oak and Barrels</div>
    </div>
    <span class="page-no">1</span>
  </section>

  <!-- 2 -->
  <section class="slide white-bg">
    <div class="photo" role="img" aria-label="Blue-tinted photo of a live-music lounge storefront at night" style="left:0;top:0;width:241px;height:68px;background:linear-gradient(180deg,#2c2f8c,#3342a0 60%,#2a3a98)"></div>
    <div class="brand" style="left:0;right:0;top:20px;justify-content:center;color:var(--white);font-size:15px"><span class="dot"></span><span class="name">BLQ</span></div>
    <div class="brand" style="left:12px;top:92px;color:var(--navy);font-size:9px"><span class="dot" style="width:6px;height:6px"></span><span class="name">BLQ</span></div>
    <div style="left:81px;top:84px;width:1px;height:37px;background:var(--navy)"></div>
    <div style="left:90px;top:97px;color:var(--navy);text-align:center">
      <div class="deck-title" style="font-size:7.5px">Your Slides Deck Name</div>
      <div class="deck-sub" style="margin-top:1px">Sub title goes here</div>
    </div>
    <span class="page-no">2</span>
  </section>

  <!-- 3 -->
  <section class="slide blue-bg">
    <div class="deco-circle" style="left:6px;top:-4px;width:160px;height:144px;border:20px solid rgba(255,255,255,.06)"></div>
    <div class="brand" style="left:31px;top:60px;color:var(--white);font-size:13px"><span class="dot" style="width:12px;height:12px"></span><span class="name">BLQ</span></div>
    <div style="left:87px;top:63px;color:var(--white);text-align:center">
      <div class="deck-title" style="font-size:8.5px">Your Slides Deck Name</div>
      <div class="deck-sub" style="margin-top:1px">Sub title goes here</div>
    </div>
    <span class="page-no light">3</span>
  </section>

  <!-- 4 -->
  <section class="slide blue-bg">
    <svg style="left:0;top:0" width="241" height="136" viewBox="0 0 241 136" aria-hidden="true">
      <path d="M107 0 C103 20 118 30 135 45 C150 58 148 80 160 100 C168 115 190 122 198 136 L241 136 L241 0 Z" fill="var(--white)"/>
    </svg>
    <div class="brand" style="right:5px;top:5px;color:var(--royal);font-size:5px"><span class="dot" style="width:5px;height:5px"></span><span class="name">BLQ</span></div>
    <div class="deck-title" style="left:9px;top:53px;color:var(--white);font-size:10.5px">Lantern Oak<br>and<br>Barrels</div>
    <div class="deck-sub" style="left:13px;top:120px;color:var(--white)">Investor deck</div>
    <span class="page-no">4</span>
  </section>

  <!-- 5 -->
  <section class="slide">
    <div class="photo" role="img" aria-label="Dimly lit banquet table set with glasses and candles" style="inset:0;background:radial-gradient(ellipse at 60% 40%,#8a8070,var(--photo-dark) 70%)"></div>
    <div style="left:38px;top:12px;width:192px;height:112px;background:rgba(24,72,176,.88)"></div>
    <div style="left:15px;top:34px;width:111px;height:69px;background:#1451b3;color:var(--white);text-align:center;padding-top:7px">
      <div class="brand" style="justify-content:center;font-size:7px"><span class="dot" style="width:6px;height:6px"></span><span class="name">BLQ</span></div>
      <div class="deck-title" style="font-size:7.5px;margin-top:5px">Lantern Oak<br>and Barrels</div>
      <div style="width:85px;height:.5px;background:rgba(255,255,255,.5);margin:4px auto 0"></div>
      <div class="deck-sub" style="margin-top:7px;font-weight:400">Investor deck</div>
    </div>
    <span class="page-no light">5</span>
  </section>

  <!-- 6 -->
  <section class="slide blue-bg">
    <div class="deco-circle" style="left:5px;top:-2px;width:160px;height:140px;border:20px solid transparent;background:linear-gradient(var(--navy),var(--navy)) padding-box,linear-gradient(180deg,#2a8a8a,#6a6a70 60%,#555) border-box;opacity:.55"></div>
    <div class="brand" style="left:34px;top:62px;color:var(--gold);font-size:11px"><span class="dot" style="width:10px;height:10px"></span><span class="name">BLQ</span></div>
    <div style="left:80px;top:63px;color:var(--gold)">
      <div class="deck-title" style="font-size:8px">Lantern Oak and Barrels</div>
      <div class="deck-sub" style="font-weight:400">Investor deck</div>
    </div>
    <span class="page-no light">6</span>
  </section>

  <!-- 7 -->
  <section class="slide white-bg">
    <div class="deco-circle" style="left:5px;top:-2px;width:160px;height:140px;border:20px solid transparent;background:linear-gradient(#fff,#fff) padding-box,linear-gradient(180deg,#9fd4cc,#f1e2b4 60%,#f4ead8) border-box;opacity:.7"></div>
    <div class="brand" style="left:34px;top:62px;color:var(--gold);font-size:11px"><span class="dot" style="width:10px;height:10px"></span><span class="name">BLQ</span></div>
    <div style="left:80px;top:63px;color:var(--gold)">
      <div class="deck-title" style="font-size:8px">Lantern Oak and Barrels</div>
      <div class="deck-sub" style="font-weight:400">Investor deck</div>
    </div>
    <span class="page-no">7</span>
  </section>

  <!-- 8 -->
  <section class="slide blue-bg">
    <div class="photo" role="img" aria-label="Festive dinner table with flowers, seen through a large circle" style="left:8px;top:6px;width:130px;height:124px;border-radius:50%;background:radial-gradient(circle at 55% 45%,#d7c8c8,#b8b0c0 45%,#6f7fb5 80%)"></div>
    <div style="left:156px;top:45px;color:var(--white)">
      <div class="card-title">Pictures, Text</div>
      <div class="card-sub">Sub title goes here</div>
      <p class="card-body">Lorem Ipsum has been the industry's standard dummy text ever since the 1500s, when an unknown printer took a galley of type and</p>
    </div>
  </section>

  <!-- 9 -->
  <section class="slide blue-bg">
    <div class="photo" role="img" aria-label="Blue-tinted banquet scene with glassware" style="inset:0;background:linear-gradient(180deg,#4a4f8f,#2f56b0 55%,var(--royal))"></div>
    <div class="deco-circle" style="left:8px;top:12px;width:126px;height:118px;border:18px solid transparent;background:linear-gradient(#2f56b0,#2f56b0) padding-box,linear-gradient(180deg,#5fb3a5,#a9c640 45%,#f2bd2a 75%,#f29a3a) border-box"></div>
    <div style="left:156px;top:45px;color:var(--white)">
      <div class="card-title">Pictures, Text</div>
      <div class="card-sub">Sub title goes here</div>
      <p class="card-body">Lorem Ipsum has been the industry's standard dummy text ever since the 1500s, when an unknown printer took a galley of type and</p>
    </div>
  </section>

  <!-- 10 -->
  <section class="slide">
    <div class="photo" role="img" aria-label="Party table under a teal-to-orange colour wash" style="inset:0;background:linear-gradient(180deg,#2a9fb0,#3aa56a 35%,#e0b22a 65%,#d15a14)"></div>
    <div class="deco-circle" style="left:8px;top:12px;width:126px;height:118px;border:18px solid rgba(20,20,30,.82)"></div>
    <div style="left:150px;top:34px;width:76px;height:68px;border-radius:8px;background:rgba(255,255,255,.14);padding:6px 0 0 6px;color:var(--white)">
      <div class="card-title">Pictures, Text</div>
      <div class="card-sub">Sub title goes here</div>
      <p class="card-body">Lorem Ipsum has been the industry's standard dummy text ever since the 1500s, when an unknown printer took a galley of type and</p>
    </div>
  </section>

  <!-- 11 -->
  <section class="slide">
    <div class="photo" role="img" aria-label="Bright wedding banquet table with pink flowers" style="inset:0;background:radial-gradient(ellipse at 70% 50%,#f3efef,var(--photo-light) 60%,#cfccd0)"></div>
    <div class="deco-circle" style="left:8px;top:12px;width:126px;height:118px;border:18px solid var(--royal)"></div>
    <div style="left:156px;top:45px;color:var(--ink)">
      <div class="card-title">Pictures, Text</div>
      <div class="card-sub">Sub title goes here</div>
      <p class="card-body">Lorem Ipsum has been the industry's standard dummy text ever since the 1500s, when an unknown printer took a galley of type and</p>
    </div>
  </section>

  <!-- 12 -->
  <section class="slide white-bg">
    <div class="photo" role="img" aria-label="Banquet table with red flowers, seen through a large circle" style="left:8px;top:12px;width:126px;height:118px;border-radius:50%;background:radial-gradient(circle at 55% 45%,#f4eeee,#d9c9c9 50%,#a39c9c 85%)"></div>
    <div style="left:156px;top:28px;width:72px;text-align:center;color:var(--navy)">
      <div class="brand" style="justify-content:center;font-size:8px"><span class="dot" style="width:7px;height:7px"></span><span class="name">BLQ</span></div>
      <div class="deck-sub" style="font-size:2.4px;font-weight:400;margin-top:1px">Lantern Oak and Barrels</div>
      <div class="card-title" style="margin-top:7px">Pictures, Text</div>
      <div class="card-sub">Sub title goes here</div>
      <p class="card-body" style="text-align:center;width:72px">Lorem Ipsum has been the industry's standard dummy text ever since the 1500s, when an unknown printer took a galley of type and</p>
    </div>
  </section>

</main>
</body>
</html>
```